Letterhead for a German Distribution/Manufacturing Company

We need a professional Letterhead in a unique Design.
not to playful.
The Letterhead has to show show that we are a international company with headquater in Germany.
all details like adress, Vat Tax Number, Bank Accout, Eori, email, Company number has to be on the Letterhead.
for example use: VAT TAX DE5704168 Bank Account: Norrfeld Bank IBAN DE421705238ß310482 Swift: KOLV3154802 EORI 3041296587 Company Number: HRB 61508 Adress: VOLTRINA UG Amsel Strasse 7 Postal Code 04683 City Kettenfeld Country: Germany Email: info@voltrina-example.com
the design can be colored but doesnt have to be
Industry/Entity Type
Manufacturing and international distribution
Requirements
Must have
- show that we are a international company with headquater in Germany. our company infos and logo

```html
<!DOCTYPE html>
<html lang="en">
<head>
<meta charset="utf-8">
<title>VOLTRINA Letterhead</title>
<link rel="stylesheet" href="https://fonts.googleapis.com/css2?family=Open+Sans:wght@400;700&display=swap">
<style>
  :root {
    --paper: #fdfdfd;
    --ink: #2a2a2a;
    --brand-dark: #3f3f3f;
    --brand-light: #5e5e5e;
    --watermark: #f0f0f0;
    --rule: #555555;
  }
  html, body {
    margin: 0;
    padding: 0;
    overflow: hidden;
    background: var(--paper);
  }
  .sheet {
    position: relative;
    width: 849px;
    height: 1200px;
    background: var(--paper);
    overflow: hidden;
    font-family: "Open Sans", Arial, sans-serif;
    color: var(--ink);
  }
  .brand-block {
    position: absolute;
    left: 56px;
    top: 44px;
    width: 180px;
    height: 105px;
    background: linear-gradient(225deg, var(--brand-light), var(--brand-dark));
    display: flex;
    align-items: center;
    justify-content: center;
    gap: 8px;
  }
  .brand-dot {
    width: 14px;
    height: 14px;
    border-radius: 50%;
    background: #ffffff;
  }
  .brand-name {
    color: #ffffff;
    font-size: 21px;
    font-weight: 400;
    letter-spacing: 0.5px;
  }
  .ref-field, .date-field {
    position: absolute;
    top: 176px;
    font-size: 9px;
    font-weight: 700;
  }
  .ref-field { left: 55px; }
  .date-field { right: 53px; }
  .field-line {
    display: inline-block;
    width: 54px;
    border-bottom: 1px dotted var(--ink);
    margin-left: 3px;
  }
  .watermark {
    position: absolute;
    left: 0;
    top: 0;
  }
  .footer-details {
    position: absolute;
    right: 53px;
    width: 420px;
    text-align: right;
    font-size: 9.4px;
    line-height: 14px;
    white-space: nowrap;
  }
  .footer-finance { top: 1060px; }
  .footer-address { top: 1116px; }
  .footer-details b { font-weight: 700; }
  .footer-rules {
    position: absolute;
    left: 0;
    top: 0;
  }
</style>
</head>
<body>
<div class="sheet">
  <svg class="watermark" width="849" height="1200" aria-hidden="true">
    <circle cx="566" cy="857" r="236" fill="var(--watermark)"/>
  </svg>

  <div class="brand-block">
    <span class="brand-dot"></span>
    <span class="brand-name">VOLTRINA</span>
  </div>

  <div class="ref-field">Ref. no. :<span class="field-line"></span></div>
  <div class="date-field">Date :<span class="field-line"></span></div>

  <div class="footer-details footer-finance">
    <div><b>VAT TAX</b> : DE5704168</div>
    <div><b>BANK ACCT.</b> : Norrfeld Bank | <b>IBAN</b> DE421705238ß310482</div>
    <div><b>SWIFT</b> KOLV3154802 | <b>EORI</b> : 3041296587</div>
  </div>

  <div class="footer-details footer-address">
    <div><b>Address :</b> VOLTRINA UG Amsel Strasse 7,</div>
    <div>City Kettenfeld,Germany-04683 | HRB 61508</div>
    <div>Email: info@voltrina-example.com</div>
  </div>

  <svg class="footer-rules" width="849" height="1200" aria-hidden="true">
    <g stroke="var(--rule)" stroke-width="1" stroke-dasharray="1 1" fill="none">
      <line x1="801" y1="1061" x2="801" y2="1157"/>
      <line x1="588" y1="1095" x2="588" y2="1157"/>
      <line x1="588" y1="1109" x2="801" y2="1109"/>
      <line x1="53" y1="1152" x2="667" y2="1152"/>
      <line x1="53" y1="1146" x2="53" y2="1158"/>
    </g>
  </svg>
</div>
</body>
</html>
```